Professional Lawn Treatment flyer (double sided) needed for established gardening company

We are an established and trusted gardening company in Swindon, UK, and are about to launch a new Lawn Treatment Service. This will be marketed to both existing and new customers and needs to reflect our current professional image. The flyer will need to be double-sided, portrait orientation and correctly sized so to be printed on A5.

If you look on our website www.pelhamgardening.co.uk, you will see our colours are purple and green. We would like you to use these exact shades of purple and green in your design.

As part of the design, we will need you to put together an infographic table to show our packages. I have attached a spreadsheet which explains these packages but I will need you to create a visually appealing table that fits in with the overall design of the flyer. I don't want you to simply cut and paste my basic table into the design.

In terms of what needs to be included, I have tried to be as specific as possible here but please feel free to message me if you need any further information or clarification.

FRONT SIDE:
The title of our service is:
Expert Lawn Treatment Service

Our strapline will need to be included somewhere:
"Lawn care by your local gardening expert"

The front side of the flyer will need to contain our logo - different versions of which can be found within my dropbox folder here...

https://www.filecrate.net/sh/k7bq24nwxe9/QWT8PmRzLxKd3VuYcH0BnJeFa?dl=0

The front side will need to contain a main image (although feel free to add more if you have anything suitable). I have included a picture in the dropbox folder titled "Front side image" which we would like used. I've also included in the folder an adobe image of grass which you may or may not like to use on either front or back.

Somewhere on both the front and back sides, you will need to include our contact details:
01632 960481
www.pelhamgardening.co.uk/lawncare

The front side should show what treatments we currently have available. These are:

- Lawn Fertilising
- Scarification
- Aeration
- Weed Control
- Moss Control
- Hydration Booster
- Kempix
- Turfing & Renovation

"Select a one-off treatment or choose from one of our specially created lawn care packages."

BACK SIDE:
On the back, we will still need our logo and contact details but the image we'd like used should be the one in the dropbox folder titled "Back side image". Again, if you have any other images you feel would also work, then please feel free to add them.

The back side is to contain a bit more information and be a bit 'wordier' and so can you please include the following 2 paragraphs:

"As expert gardeners, we are passionate about horticulture and working to bring out the very best in your garden. When we work in your garden, we look at it and treat it with the same care and attention as if it were our own, before handing it back for you to enjoy. Our passion doesn't end at just trees and shrubs though. Your grass is as much of a living, breathing plant as your shrubs and we therefore utilise our expert horticultural knowledge to ensure your lawn thrives and reaches its fullest potential.

Lawn care isn't just about applying a fertiliser. It's about really understanding your lawn and being able to use extensive knowledge and experience to diagnose and treat issues. It therefore stands to reason that you should employ an expert to bring out the best in your lawn which is why we at Pelham Gardening Services have created a superior lawn care service that will keep your lawn looking lush, green and healthy all year round."

I referred at the very top of this brief to the fact we will need an infographic table created to show the different lawn care packages available. You see from the PDF table I created that we have 3 packages; Standard, Enhanced and Premium. Please create a visually appealing table which sets out the differences between our packages and include it on the back page.

Finally, somewhere we would like reference to the other gardening services we do. It's only to be something small as it isn't the main focus of the flyer but we think it would be good to mention what else we do. To re-iterate, it isnt to be big. I still want the main focus to be lawn care but if you could somehow reference that we also do the following services, that would be good. I will leave it to you to decide where on the flyer it fits in best, be it the front or back:

- Lawn mowing
- Shrub pruning
- Hedge trimming
- Weed killing
- Garden clearance & tidy-up
- Planting & design
- Regular Garden Maintenance
- Turfing
- Fencing
- Gutter clearance

I think thats it. I look forward to your designs!
Ps. Don't forget the dropbox folder:

Target Market(s)

Professional men/women aged 25+
Retired aged 65+

Industry/Entity Type

Home And Garden

Font styles to use
Sans Serif

Colors
6b449b
9bcb3c

Requirements
Must have
• Our company colours; purple and green; as per our website www.pelhamgardening.co.uk. I've selected purple and green on this brief just to highlight the colours needed but please be sure to use the exact shades from our website and NOT the shade of purple and green that were selected on this brief.
• All the wording as explained in the main project brief.
Nice to have
• I want the flyer to be bold, eye-catching and modern.
• We particularly like the font Trebuchet MS for general copy but please feel free to use any other font for bolder, main titles.
Should not have
• We don't want anything gimmicky. No cheesy marketing.
• We only want professional looking designs. With the greatest of respect, if you're just starting out or don't really do design but think you'll use this as practise, please don't waste your or our time. We've previously run contests for other projects where we've had designs submitted that have clearly been done on MS Word and used Clipart and Wordart. That's really not what we are looking for.

```html
<!DOCTYPE html>
<html lang="en">
<head>
<meta charset="utf-8">
<title>Pelham Gardening Services – Expert Lawn Treatment Service</title>
<link rel="stylesheet" href="https://fonts.googleapis.com/css2?family=PT+Sans:wght@400;700&family=Roboto+Condensed:wght@400;700&display=swap">
<style>
  :root {
    --maroon: #8b1a35;
    --green: #3ab54a;
    --lawn-light: #6cc53a;
    --lawn-dark: #3c9422;
    --paving: #d8cfc2;
    --gold: #c3a035;
    --brown: #3b2418;
    --ink: #231f20;
    --white: #ffffff;
    --page: #e6e6e6;
    --rule: #cfe8c9;
  }
  html, body {
    margin: 0;
    padding: 0;
    width: 1200px;
    height: 1200px;
    overflow: hidden;
    background: var(--page);
  }
  .flyer {
    position: absolute;
    left: 166px;
    top: 40px;
    width: 867px;
    height: 1120px;
    box-shadow: 0 6px 24px rgba(0,0,0,0.25);
    background: var(--white);
  }
  .flyer svg { display: block; width: 100%; height: 100%; }
  .headline { font-family: "PT Sans", sans-serif; fill: var(--white); }
  .service-title { font-family: "Roboto Condensed", sans-serif; font-weight: 700; fill: var(--ink); }
  .treatment { font-family: "Roboto Condensed", sans-serif; font-size: 22px; fill: var(--ink); }
  .brand-name { font-family: "Roboto Condensed", sans-serif; font-weight: 400; fill: var(--brown); }
  .contact { font-family: "Roboto Condensed", sans-serif; fill: var(--white); }
</style>
</head>
<body>
<div class="flyer">
  <svg viewBox="0 0 926 1196" xmlns="http://www.w3.org/2000/svg">
    <defs>
      <linearGradient id="lawn-photo" x1="0" y1="0" x2="1" y2="1">
        <stop offset="0" stop-color="var(--lawn-light)"/>
        <stop offset="0.42" stop-color="var(--paving)"/>
        <stop offset="0.58" stop-color="var(--lawn-light)"/>
        <stop offset="1" stop-color="var(--lawn-dark)"/>
      </linearGradient>
      <linearGradient id="soft-shadow" x1="0" y1="0" x2="0" y2="1">
        <stop offset="0" stop-color="#000" stop-opacity="0.14"/>
        <stop offset="1" stop-color="#000" stop-opacity="0"/>
      </linearGradient>
      <clipPath id="page-clip"><rect width="926" height="1196"/></clipPath>
    </defs>

    <g clip-path="url(#page-clip)">
      <!-- header band -->
      <path class="header-shadow" d="M520 300 C650 345 780 372 926 380 V440 C780 430 640 400 520 340 Z" fill="url(#soft-shadow)"/>
      <path class="header-green" d="M520 230 C650 275 780 302 926 312 V372 C780 360 650 330 520 290 Z" fill="var(--green)"/>
      <path class="header-band" d="M0 0 H926 V312 C780 302 650 275 520 230 L0 230 Z" fill="var(--maroon)"/>
      <path class="corner-accent" d="M0 0 H55 L30 34 Z" fill="var(--green)"/>

      <!-- headline -->
      <g class="headline" text-anchor="end">
        <text x="875" y="88" font-size="60">Lawn care</text>
        <text x="893" y="145" font-size="44">by your local</text>
        <text x="893" y="202" font-size="60">Gardening</text>
        <text x="893" y="258" font-size="60">Expert</text>
      </g>

      <!-- service title bar -->
      <rect class="title-bar-shadow" x="393" y="626" width="503" height="40" fill="url(#soft-shadow)"/>
      <rect class="title-bar" x="393" y="552" width="503" height="74" fill="var(--gold)"/>
      <text class="service-title" x="886" y="598" font-size="32" text-anchor="end">Expert Lawn Treatment Service</text>

      <!-- hero image frame -->
      <circle class="frame-ring" cx="215" cy="348" r="335" fill="var(--brown)"/>
      <circle class="frame-mat" cx="190" cy="340" r="326" fill="var(--white)"/>
      <circle class="hero-image" cx="175" cy="345" r="311" fill="url(#lawn-photo)" role="img" aria-label="Photo of a neatly striped green lawn with a curving stone paved path"/>

      <!-- treatments list -->
      <g class="treatments">
        <line x1="488" y1="672" x2="488" y2="970" stroke="var(--green)" stroke-width="1.5"/>
        <g stroke="var(--rule)" stroke-width="1">
          <line x1="488" y1="705" x2="710" y2="705"/>
          <line x1="488" y1="743" x2="710" y2="743"/>
          <line x1="488" y1="781" x2="710" y2="781"/>
          <line x1="488" y1="819" x2="710" y2="819"/>
          <line x1="488" y1="857" x2="710" y2="857"/>
          <line x1="488" y1="895" x2="710" y2="895"/>
          <line x1="488" y1="932" x2="710" y2="932"/>
        </g>
        <g fill="var(--ink)">
          <circle cx="476" cy="685" r="4"/><circle cx="476" cy="723" r="4"/>
          <circle cx="476" cy="761" r="4"/><circle cx="476" cy="799" r="4"/>
          <circle cx="476" cy="837" r="4"/><circle cx="476" cy="875" r="4"/>
          <circle cx="476" cy="912" r="4"/><circle cx="476" cy="950" r="4"/>
        </g>
        <text class="treatment" x="495" y="693">Lawn Fertilising</text>
        <text class="treatment" x="495" y="731">Scarification</text>
        <text class="treatment" x="495" y="769">Aeration</text>
        <text class="treatment" x="495" y="807">Weed Control</text>
        <text class="treatment" x="495" y="845">Moss Control</text>
        <text class="treatment" x="495" y="883">Hydration Booster</text>
        <text class="treatment" x="495" y="920">Kempix</text>
        <text class="treatment" x="495" y="958">Turfing &amp; Renovation</text>
      </g>

      <!-- brand name -->
      <g class="brand">
        <circle cx="136" cy="898" r="26" fill="var(--green)"/>
        <text class="brand-name" x="52" y="1004" font-size="92" textLength="312" lengthAdjust="spacingAndGlyphs">Pelham</text>
        <text class="brand-name" x="72" y="1030" font-size="22" letter-spacing="3" textLength="292" lengthAdjust="spacing">GARDENING SERVICES</text>
      </g>

      <!-- footer band -->
      <path class="footer-shadow" d="M0 1118 C250 1108 500 990 926 975 V995 C500 1010 250 1120 0 1126 Z" fill="#d9d2d4"/>
      <path class="footer-band" d="M0 1126 C250 1120 500 1010 926 995 V1196 H0 Z" fill="var(--maroon)"/>
      <g class="contact" text-anchor="end">
        <text x="888" y="1126" font-size="46">Contact us 01632 960481</text>
        <text x="888" y="1166" font-size="31">www.pelhamgardening.co.uk/lawncare</text>
      </g>
    </g>
  </svg>
</div>
</body>
</html>
```